Business Card design for construction company

I would like a business card design for a construction company - Harlow Constructions. I have attached the ai logo file for use. I would like the card to be very smart and clean and incorporate only white and the two colours in the logo. I would like the card to have two sides. One side can just have the logo, the other with the relevant information.

Target Market(s)

Building and Construction Clients

Industry/Entity Type

Business

Contact Information for Business Card

Name: Tom Pardoe
Company: Harlow Constructions Pty Limited
Address: 14 Mallee Crescent Carrow Vale 2093
Phone: 0427 531 068
Email: tomp@harlowbuild-example.com.au

Font styles to use
Serif
Sans Serif

Requirements
Must have
• Details noted above
• Logo as provided
• Colours as in logo
• Square edges
• A font that compliments the logo
Should not have
• Any colour other than white and those in logo
• Rounded edges

```html
<!DOCTYPE html>
<html lang="en">
<head>
<meta charset="utf-8">
<title>Harlow Constructions – Business Card</title>
<link rel="stylesheet" href="https://fonts.googleapis.com/css2?family=Open+Sans:wght@400;600;700&display=swap">
<style>
  :root {
    --backdrop: #262626;
    --kraft-light: #dcbf98;
    --kraft-mid: #c8a57a;
    --kraft-dark: #a8815a;
    --ink: #2a241d;
    --rule: rgba(42, 36, 29, 0.35);
  }
  * { box-sizing: border-box; margin: 0; padding: 0; }
  html, body {
    width: 1200px;
    height: 900px;
    overflow: hidden;
    background: var(--backdrop);
    font-family: "Open Sans", Arial, sans-serif;
    color: var(--ink);
  }
  .canvas {
    position: relative;
    width: 1200px;
    height: 900px;
  }
  .card {
    position: absolute;
    top: 306px;
    width: 440px;
    height: 271px;
    background: linear-gradient(135deg, var(--kraft-light) 0%, var(--kraft-mid) 55%, var(--kraft-dark) 100%);
  }
  .card--details { left: 149px; }
  .card--logo { left: 608px; }

  .wordmark {
    position: absolute;
    left: 0;
    right: 0;
    text-align: center;
    font-size: 20px;
    font-weight: 400;
    letter-spacing: 0.14em;
    text-transform: uppercase;
    white-space: nowrap;
  }
  .card--details .wordmark { top: 63px; }
  .card--logo .wordmark { top: 122px; }

  .card__rule {
    position: absolute;
    left: 31px;
    right: 25px;
    top: 166px;
    border-top: 1px solid var(--rule);
  }

  .contact {
    position: absolute;
    left: 31px;
    top: 184px;
  }
  .contact__name {
    font-size: 17px;
    font-weight: 700;
    letter-spacing: 0.01em;
    text-transform: uppercase;
    line-height: 22px;
    margin-bottom: 4px;
  }
  .contact__line {
    display: flex;
    align-items: center;
    gap: 6px;
    font-size: 12px;
    line-height: 17px;
  }
  .contact__icon { width: 8px; height: 10px; flex: none; }

  .company {
    position: absolute;
    right: 24px;
    top: 191px;
    text-align: right;
    font-size: 13px;
    line-height: 18px;
  }
  .company__name { font-weight: 600; }
</style>
</head>
<body>
<div class="canvas">
  <section class="card card--details">
    <div class="wordmark">Harlow Constructions</div>
    <div class="card__rule"></div>

    <div class="contact">
      <p class="contact__name">Tom Pardoe</p>
      <p class="contact__line">
        <svg class="contact__icon" viewBox="0 0 8 10" aria-hidden="true">
          <rect x="1" y="0.5" width="6" height="9" rx="1" fill="none" stroke="currentColor" stroke-width="1"/>
          <rect x="3" y="7.5" width="2" height="1" fill="currentColor"/>
        </svg>
        0427 531 068
      </p>
      <p class="contact__line">
        <svg class="contact__icon" viewBox="0 0 8 10" aria-hidden="true">
          <rect x="0" y="2" width="8" height="6" fill="currentColor"/>
          <path d="M0 2 L4 5.5 L8 2" fill="none" stroke="#c8a57a" stroke-width="0.9"/>
        </svg>
        tomp@harlowbuild-example.com.au
      </p>
    </div>

    <div class="company">
      <p class="company__name">Harlow Constructions Pty Limited</p>
      <p>14 Mallee Crescent Carrow</p>
      <p>Vale 2093</p>
    </div>
  </section>

  <section class="card card--logo">
    <div class="wordmark">Harlow Constructions</div>
  </section>
</div>
</body>
</html>
```